Veltrona Services

Double sided business cards with color on front and black and white on back. I have basic ideas and graphics, but am looking for someone to take them to the next level

```html
<!DOCTYPE html>
<html lang="en">
<head>
<meta charset="utf-8">
<title>Veltrona Services – Business Card</title>
<link rel="stylesheet" href="https://fonts.googleapis.com/css2?family=Bebas+Neue&family=Lato:wght@400&display=swap">
<style>
  :root {
    --page-bg: #e4e4e4;
    --white: #ffffff;
    --black: #000000;
    --ink: #1c1c1c;
    --accent-orange: #ee6a2c;
    --accent-violet: #6a4fb0;
    --grad-blue: #3e6fc4;
    --grad-purple: #6a4fa8;
    --grad-yellow: #f5d52a;
    --grad-orange: #f08a2a;
    --grad-red: #e8303f;
    --grad-magenta: #d42f7a;
    --grad-mauve: #b35a9e;
    --grad-green: #8bb35a;
    --card-shadow: 0 6px 14px rgba(0,0,0,0.35);
  }
  html, body {
    margin: 0;
    padding: 0;
    width: 1200px;
    height: 1200px;
    overflow: hidden;
    background: var(--page-bg);
  }
  .sheet {
    position: relative;
    width: 1200px;
    height: 1200px;
  }
  .card {
    position: absolute;
    height: 477px;
    border-radius: 19px;
    overflow: hidden;
    box-shadow: var(--card-shadow);
  }
  .card-front { left: 189px; top: 91px; width: 829px; }
  .card-back  { left: 187px; top: 639px; width: 834px; }
  .card-art {
    position: absolute;
    inset: 0;
    width: 100%;
    height: 100%;
  }
  .title, .tagline, .brand-name {
    font-family: "Bebas Neue", "Oswald", sans-serif;
    font-weight: 400;
    margin: 0;
    text-transform: uppercase;
  }
  .front-info {
    position: absolute;
    left: 500px;
    width: 310px;
    top: 0;
    text-align: center;
    color: var(--white);
  }
  .title {
    position: absolute;
    left: 0;
    width: 100%;
    font-size: 78px;
    line-height: 1;
    letter-spacing: 0.5px;
  }
  .title-line-1 { top: 101px; }
  .title-line-2 { top: 178px; }
  .phone-icon {
    position: absolute;
    left: 122px;
    top: 259px;
    width: 66px;
    height: 66px;
  }
  .phone-number {
    position: absolute;
    left: 0;
    width: 100%;
    top: 334px;
    font-family: "Lato", sans-serif;
    font-size: 39px;
    line-height: 1;
    letter-spacing: 0.5px;
  }
  .front-brand {
    position: absolute;
    left: 85px;
    top: 210px;
    width: 300px;
    display: flex;
    align-items: center;
    gap: 12px;
  }
  .brand-dot {
    width: 34px;
    height: 34px;
    border-radius: 50%;
    flex: none;
  }
  .front-brand .brand-dot { background: var(--accent-violet); }
  .front-brand .brand-name { color: var(--ink); font-size: 56px; line-height: 1; }
  .back-copy {
    position: absolute;
    left: 29px;
    width: 300px;
    top: 0;
    text-align: center;
    color: var(--white);
  }
  .tagline {
    position: absolute;
    left: 0;
    width: 100%;
    font-size: 66px;
    line-height: 1;
  }
  .tagline-1 { top: 55px; }
  .tagline-2 { top: 133px; }
  .tagline-3 { top: 211px; }
  .tagline-4 { top: 290px; }
  .tagline-5 { top: 368px; }
  .back-brand {
    position: absolute;
    left: 446px;
    top: 211px;
    width: 300px;
    display: flex;
    align-items: center;
    justify-content: center;
    gap: 12px;
  }
  .back-brand .brand-dot { background: var(--black); }
  .back-brand .brand-name { color: var(--black); font-size: 56px; line-height: 1; }
</style>
</head>
<body>
<main class="sheet">

  <section class="card card-front" aria-label="Business card front">
    <svg class="card-art" viewBox="0 0 829 477" preserveAspectRatio="none" aria-hidden="true">
      <defs>
        <linearGradient id="spectrum" x1="0.35" y1="1" x2="1" y2="0">
          <stop offset="0" stop-color="var(--grad-blue)"/>
          <stop offset="0.14" stop-color="var(--grad-purple)"/>
          <stop offset="0.32" stop-color="var(--grad-yellow)"/>
          <stop offset="0.45" stop-color="var(--grad-orange)"/>
          <stop offset="0.56" stop-color="var(--grad-red)"/>
          <stop offset="0.74" stop-color="var(--grad-magenta)"/>
          <stop offset="0.9" stop-color="var(--grad-mauve)"/>
          <stop offset="1" stop-color="var(--grad-green)"/>
        </linearGradient>
      </defs>
      <rect class="spectrum-field" width="829" height="477" fill="url(#spectrum)"/>
      <rect class="white-panel" width="243" height="477" fill="var(--white)"/>
      <circle class="white-disc" cx="243" cy="240" r="247" fill="var(--white)"/>
    </svg>

    <div class="front-brand">
      <span class="brand-dot"></span>
      <p class="brand-name">Veltrona</p>
    </div>

    <div class="front-info">
      <h1 class="title title-line-1">Veltrona</h1>
      <h1 class="title title-line-2">Services</h1>
      <svg class="phone-icon" viewBox="0 0 66 66" aria-hidden="true">
        <circle cx="33" cy="33" r="33" fill="var(--white)"/>
        <path d="M22 17c2-1 4 0 5 2l3 6c1 2 0 3-1 4l-2 2c1 4 5 8 9 10l2-2c1-1 3-2 4-1l6 3c2 1 3 3 2 5l-2 3c-2 2-5 3-8 2-10-3-18-11-21-21-1-3 0-6 2-8z" fill="var(--accent-orange)"/>
        <path d="M36 20a11 11 0 0 1 10 10M36 13a18 18 0 0 1 17 17" fill="none" stroke="var(--accent-orange)" stroke-width="3.2" stroke-linecap="round"/>
      </svg>
      <p class="phone-number">555-014-2738</p>
    </div>
  </section>

  <section class="card card-back" aria-label="Business card back">
    <svg class="card-art" viewBox="0 0 834 477" preserveAspectRatio="none" aria-hidden="true">
      <rect class="black-field" width="834" height="477" fill="var(--black)"/>
      <rect class="white-panel" x="594" width="240" height="477" fill="var(--white)"/>
      <circle class="white-disc" cx="594" cy="239" r="248" fill="var(--white)"/>
    </svg>

    <div class="back-copy">
      <p class="tagline tagline-1">A Curated</p>
      <p class="tagline tagline-2">Experience</p>
      <p class="tagline tagline-3">All That</p>
      <p class="tagline tagline-4">Is Promised</p>
      <p class="tagline tagline-5">Is Clarity</p>
    </div>

    <div class="back-brand">
      <span class="brand-dot"></span>
      <p class="brand-name">Veltrona</p>
    </div>
  </section>

</main>
</body>
</html>
```